High end Security Alarm company needs an elegant business card design.

We need an elegant, "corporate looking" business card. It CANNOT look like a mom and pop design or have too many colors.
This business card will be handed to business owners as well as high end customers that will be paying a lot of money for our services. So it has to look very professional.
The services that i want list on the card are: Security Systems, Security cameras (CCTV), Access Control, Networking and Smart Homes
Phone numbers:
(800)613-4078
(917)402-3861
Website:
kestronalarms.com
Email:
dominik@kestronalarms.com
My name is Dom Tarv - I do not want any position to be indicated (general manager, sales, etc...)
No company address.
Make sure that designs are compatible with CardNest and Zib.
Our logo files have been attached and would like our color scheme to revolve around our logo.
All designs must be submitted by 5pm e.t. on July 5. No Designs will be accepted after that time.

```html
<!DOCTYPE html>
<html lang="en">
<head>
<meta charset="utf-8">
<title>Kestron – Business Card</title>
<link href="https://fonts.googleapis.com/css2?family=Roboto+Condensed:wght@400;700&display=swap" rel="stylesheet">
<style>
  :root {
    --orange: #e8620c;
    --ink: #2b2b2b;
    --grey: #4a4a4a;
    --paper: #ffffff;
    --backdrop: #e9e6e1;
  }
  * { margin: 0; padding: 0; box-sizing: border-box; }
  html, body { width: 1200px; height: 800px; overflow: hidden; }
  body {
    background: var(--backdrop);
    font-family: "Roboto Condensed", "Arial Narrow", sans-serif;
    color: var(--ink);
    display: flex;
    align-items: center;
    justify-content: center;
    gap: 48px;
  }
  .card {
    position: relative;
    width: 540px;
    height: 308px;
    background: var(--paper);
    box-shadow: 0 6px 22px rgba(0,0,0,.18);
    overflow: hidden;
  }

  /* Brand name: one colour, one weight, plain square beside it */
  .brand { position: absolute; display: flex; align-items: center; gap: 12px; }
  .brand-square { width: 18px; height: 18px; background: var(--orange); flex: none; }
  .brand-name {
    font-weight: 700; color: var(--ink);
    font-size: 40px; line-height: 1; letter-spacing: 1px;
  }

  /* Front */
  .accent { position: absolute; background: var(--orange); height: 30px; }
  .accent--top { top: 22px; right: 0; width: 78px; }
  .accent--bottom { bottom: 22px; left: 0; width: 78px; }
  .front .brand { left: 118px; top: 100px; }
  .services {
    position: absolute; left: 118px; top: 172px; width: 400px;
    font-size: 17px; line-height: 1.35; color: var(--grey);
  }

  /* Back */
  .back .brand { left: 34px; top: 40px; }
  .back .brand-name { font-size: 34px; }
  .holder { position: absolute; left: 34px; top: 150px; font-size: 21px; color: var(--grey); }
  .contacts {
    position: absolute; left: 150px; top: 150px;
    list-style: none; font-size: 18px; color: var(--ink);
  }
  .contacts li { display: flex; align-items: center; gap: 10px; height: 30px; }
  .contacts svg { width: 22px; height: 22px; flex: none; }
  .band {
    position: absolute; left: 0; right: 0; bottom: 22px; height: 44px;
    background: var(--orange); color: var(--paper);
    font-size: 22px; letter-spacing: 1px;
    display: flex; align-items: center; justify-content: flex-end; padding-right: 30px;
  }
</style>
</head>
<body>

  <section class="card front">
    <div class="accent accent--top"></div>
    <div class="accent accent--bottom"></div>
    <div class="brand">
      <span class="brand-square"></span>
      <span class="brand-name">KESTRON</span>
    </div>
    <p class="services">Security Systems | Security Cameras (CCTV) | Access Control | Video Intercom | Networking | Smart Homes</p>
  </section>

  <section class="card back">
    <div class="brand">
      <span class="brand-name">KESTRON</span>
    </div>
    <p class="holder">Dom Tarv</p>
    <ul class="contacts">
      <li>
        <svg viewBox="0 0 22 22" aria-hidden="true"><circle cx="11" cy="11" r="11" fill="#e8620c"/><path d="M7 6h3l1 3-1.5 1a6 6 0 0 0 2.5 2.5L13 11l3 1v3a1 1 0 0 1-1 1A9 9 0 0 1 6 7a1 1 0 0 1 1-1z" fill="#fff"/></svg>
        (800)613-4078
      </li>
      <li>
        <svg viewBox="0 0 22 22" aria-hidden="true"><circle cx="11" cy="11" r="11" fill="#e8620c"/><rect x="7.5" y="5" width="7" height="12" rx="1.2" fill="none" stroke="#fff" stroke-width="1.5"/><circle cx="11" cy="15" r=".9" fill="#fff"/></svg>
        (917)402-3861
      </li>
      <li>
        <svg viewBox="0 0 22 22" aria-hidden="true"><circle cx="11" cy="11" r="11" fill="#e8620c"/><rect x="5.5" y="7" width="11" height="8" fill="none" stroke="#fff" stroke-width="1.4"/><path d="M5.5 7l5.5 4.5L16.5 7" fill="none" stroke="#fff" stroke-width="1.4"/></svg>
        dominik@kestronalarms.com
      </li>
    </ul>
    <div class="band">www.kestronalarms.com</div>
  </section>

</body>
</html>
```